Assorted Banner Ads

Create standard sized banner ads (300x250, 728x90, 160x600) using logo and create exciting ads using collateral provided and your own ideas.

```html
<!DOCTYPE html>
<html lang="en">
<head>
<meta charset="utf-8">
<title>Harbor Point Room Escape – Banner Set</title>
<link rel="stylesheet" href="https://fonts.googleapis.com/css2?family=Poppins:wght@500;600&family=Oswald:wght@300;400&family=Roboto:wght@700&display=swap">
<style>
  :root{
    --green:#2e8b45;
    --green-bright:#3aa354;
    --bullet:#7fc98f;
    --dark:#262626;
    --frame:#4a4a4a;
    --white:#ffffff;
    --ink:#2a2a2a;
    --text-light:#e6e6e6;
    --photo-a:#46524c;
    --photo-b:#1d2622;
  }
  *{box-sizing:border-box;margin:0;padding:0}
  html,body{width:1200px;height:1200px;overflow:hidden;background:var(--white)}
  .sheet{position:relative;width:1200px;height:1200px;background:var(--white)}
  .sheet-band{position:absolute;left:0;width:1200px;height:10px;background:var(--green)}
  .sheet-band--top{top:0}
  .sheet-band--bottom{bottom:0}

  .banner{position:absolute;box-shadow:3px 4px 8px rgba(0,0,0,.35);overflow:hidden}
  .banner-inner{position:absolute;left:0;top:0;transform:scale(1.25);transform-origin:0 0;background:var(--dark);overflow:hidden}
  .banner-shapes{position:absolute;left:0;top:0}

  .headline{position:absolute;font-family:"Poppins",sans-serif;font-weight:600;color:var(--white);line-height:1.2;letter-spacing:-.2px}
  .headline em{font-style:normal;color:var(--green-bright)}

  .room-list{position:absolute;list-style:none;font-family:"Oswald",sans-serif;font-weight:300;color:var(--text-light)}
  .room-list li{position:relative;padding-left:14px;white-space:nowrap}
  .room-list li::before{content:"";position:absolute;left:0;top:50%;width:7px;height:7px;margin-top:-4px;border-radius:50%;background:var(--bullet);border:1px solid var(--white)}

  .cta{position:absolute;display:flex;align-items:center;justify-content:center;gap:5px;background:var(--green);border-radius:3px;font-family:"Roboto",sans-serif;font-weight:700;color:var(--white);white-space:nowrap}
  .cta-icon{display:block}

  .brand{position:absolute;display:flex;flex-direction:column;align-items:center;text-align:center}
  .brand-mark{width:12px;height:12px;background:var(--green);margin-bottom:4px}
  .brand-name{font-family:"Poppins",sans-serif;font-weight:600;color:var(--ink);line-height:1.15;text-transform:uppercase}

  /* 728 x 90 */
  .banner--leaderboard{left:145px;top:125px;width:910px;height:113px}
  .banner--leaderboard .banner-inner{width:728px;height:90px}
  .banner--leaderboard .headline{left:235px;top:8px;font-size:16.5px}
  .banner--leaderboard .room-list{top:38px;font-size:12px}
  .banner--leaderboard .room-list li{height:19px;line-height:19px}
  .banner--leaderboard .room-list--a{left:238px}
  .banner--leaderboard .room-list--b{left:357px}
  .banner--leaderboard .cta{left:504px;top:39px;width:106px;height:29px;font-size:11.5px}
  .banner--leaderboard .brand{left:630px;top:32px;width:96px}
  .banner--leaderboard .brand-name{font-size:9px}

  /* 300 x 250 */
  .banner--rectangle{left:145px;top:325px;width:375px;height:313px}
  .banner--rectangle .banner-inner{width:300px;height:250px}
  .banner--rectangle .headline{right:21px;top:14px;font-size:17.5px;text-align:right}
  .banner--rectangle .room-list{left:170px;top:73px;font-size:12.5px}
  .banner--rectangle .room-list li{height:23.5px;line-height:23.5px}
  .banner--rectangle .cta{left:167px;top:189px;width:122px;height:33px;font-size:13px}
  .banner--rectangle .brand{left:6px;top:196px;width:118px}
  .banner--rectangle .brand-name{font-size:9.5px}

  /* 160 x 600 */
  .banner--skyscraper{left:600px;top:325px;width:200px;height:750px}
  .banner--skyscraper .banner-inner{width:160px;height:600px}
  .banner--skyscraper .headline{left:0;width:160px;top:263px;font-size:16px;text-align:center}
  .banner--skyscraper .room-list{left:15px;top:323px;font-size:12.5px}
  .banner--skyscraper .room-list li{height:23.5px;line-height:23.5px}
  .banner--skyscraper .cta{left:19px;top:434px;width:122px;height:34px;font-size:13px}
  .banner--skyscraper .brand{left:28px;top:528px;width:120px}
  .banner--skyscraper .brand-name{font-size:9.5px}
</style>
</head>
<body>
<main class="sheet">
  <div class="sheet-band sheet-band--top"></div>

  <!-- Leaderboard 728x90 -->
  <section class="banner banner--leaderboard" aria-label="Leaderboard banner">
    <div class="banner-inner">
      <svg class="banner-shapes" width="728" height="90" viewBox="0 0 728 90">
        <defs>
          <linearGradient id="photoLb" x1="0" y1="0" x2="1" y2="1">
            <stop offset="0" stop-color="var(--photo-a)"/>
            <stop offset="1" stop-color="var(--photo-b)"/>
          </linearGradient>
        </defs>
        <path role="img" aria-label="Photo of a rusted padlock hanging on a chain" d="M0,0 H190 C206,0 212,18 214,40 L219,90 H0 Z" fill="url(#photoLb)"/>
        <path d="M190,0 C206,0 212,18 214,40 L219,90" fill="none" stroke="var(--green)" stroke-width="6"/>
        <path d="M728,0 L715,3 C680,12 648,14 634,32 C624,46 622,68 624,90 H728 Z" fill="var(--white)"/>
      </svg>
      <h2 class="headline">Can you Escape in <em>60 Minutes?</em></h2>
      <ul class="room-list room-list--a"><li>The Locked Library</li><li>Harbor Jail Break</li></ul>
      <ul class="room-list room-list--b"><li>Sunken Treasure Hunt</li><li>Lighthouse Escape</li></ul>
      <a class="cta">READ MORE
        <svg class="cta-icon" width="14" height="14" viewBox="0 0 14 14"><circle cx="7" cy="7" r="7" fill="var(--white)"/><path d="M5.8,4 L8.8,7 L5.8,10" fill="none" stroke="var(--green)" stroke-width="1.8"/></svg>
      </a>
      <div class="brand"><span class="brand-mark"></span><span class="brand-name">Harbor Point<br>Room Escape</span></div>
    </div>
  </section>

  <!-- Medium rectangle 300x250 -->
  <section class="banner banner--rectangle" aria-label="Medium rectangle banner">
    <div class="banner-inner">
      <svg class="banner-shapes" width="300" height="250" viewBox="0 0 300 250">
        <defs>
          <linearGradient id="photoMr" x1="0" y1="0" x2="1" y2="1">
            <stop offset="0" stop-color="var(--photo-a)"/>
            <stop offset="1" stop-color="var(--photo-b)"/>
          </linearGradient>
        </defs>
        <rect x="67" y="5" width="227" height="240" fill="none" stroke="var(--frame)" stroke-width="1"/>
        <path role="img" aria-label="Photo of a rusted padlock hanging on a chain" d="M0,0 H66 L150,118 C166,142 164,170 150,200 L132,250 H0 Z" fill="url(#photoMr)"/>
        <path d="M66,0 L150,118 C166,142 164,170 150,200 L132,250" fill="none" stroke="var(--green)" stroke-width="6"/>
        <path d="M0,196 C22,180 60,170 86,180 C112,190 126,220 136,250 H0 Z" fill="var(--white)"/>
      </svg>
      <h2 class="headline">Can you Escape<br>in <em>60 Minutes?</em></h2>
      <ul class="room-list"><li>The Locked Library</li><li>Harbor Jail Break</li><li>Sunken Treasure Hunt</li><li>Lighthouse Escape</li></ul>
      <a class="cta">READ MORE
        <svg class="cta-icon" width="15" height="15" viewBox="0 0 14 14"><circle cx="7" cy="7" r="7" fill="var(--white)"/><path d="M5.8,4 L8.8,7 L5.8,10" fill="none" stroke="var(--green)" stroke-width="1.8"/></svg>
      </a>
      <div class="brand"><span class="brand-mark"></span><span class="brand-name">Harbor Point<br>Room Escape</span></div>
    </div>
  </section>

  <!-- Wide skyscraper 160x600 -->
  <section class="banner banner--skyscraper" aria-label="Skyscraper banner">
    <div class="banner-inner">
      <svg class="banner-shapes" width="160" height="600" viewBox="0 0 160 600">
        <defs>
          <linearGradient id="photoSk" x1="0" y1="0" x2="1" y2="1">
            <stop offset="0" stop-color="var(--photo-a)"/>
            <stop offset="1" stop-color="var(--photo-b)"/>
          </linearGradient>
        </defs>
        <rect x="4" y="205" width="150" height="320" fill="none" stroke="var(--frame)" stroke-width="1"/>
        <path role="img" aria-label="Photo of a rusted padlock hanging on a chain" d="M0,0 H160 V180 L58,222 C38,232 18,228 8,210 L0,192 Z" fill="url(#photoSk)"/>
        <path d="M160,180 L58,222 C38,232 18,228 8,210 L0,192" fill="none" stroke="var(--green)" stroke-width="6"/>
        <path d="M0,540 L104,516 C134,509 154,540 160,572 V600 H0 Z" fill="var(--white)"/>
      </svg>
      <h2 class="headline">Can you Escape<br>in <em>60 Minutes?</em></h2>
      <ul class="room-list"><li>The Locked Library</li><li>Harbor Jail Break</li><li>Sunken Treasure Hunt</li><li>Lighthouse Escape</li></ul>
      <a class="cta">READ MORE
        <svg class="cta-icon" width="15" height="15" viewBox="0 0 14 14"><circle cx="7" cy="7" r="7" fill="var(--white)"/><path d="M5.8,4 L8.8,7 L5.8,10" fill="none" stroke="var(--green)" stroke-width="1.8"/></svg>
      </a>
      <div class="brand"><span class="brand-mark"></span><span class="brand-name">Harbor Point<br>Room Escape</span></div>
    </div>
  </section>

  <div class="sheet-band sheet-band--bottom"></div>
</main>
</body>
</html>
```